Billboard design for agricultural machinery business

hello im looking for roadside advertiement sign to be designed, the sign is 10ft up in the air and is 4ft high and 8ft wide, id image i like a blue background and my logo front and centre and below logo sales - service - parts and then below that the brook meadow symbol and vale symbol, I’d also like the website www.Fernowell.ie on it. i am open to suggestions and designs. blue is #005999 and yellow is rgb (254, 205, 26) ive attached my log and symbols, im open to different colour backgrounds or just white and also open to brook meadow and vale as writhing rather than logos

Target Market(s)

Brook Meadow and vale tractor owners

Industry/Entity Type

Agricultural machine sales service and parts

Colors

Designer to choose colors to be used in the design.

Requirements
Must have
• My logo and colours, brands brook Meadow and vale, website

```html
<!DOCTYPE html>
<html lang="en">
<head>
<meta charset="UTF-8">
<title>Fernowell roadside sign</title>
<link href="https://fonts.googleapis.com/css2?family=Montserrat:wght@600;700;800&display=swap" rel="stylesheet">
<style>
  :root {
    --backdrop: #b5b1b0;
    --brand-blue: #005999;
    --brand-yellow: #fecd1a;
    --white: #ffffff;
    --ink: #1d1d1b;
  }
  * { margin: 0; padding: 0; box-sizing: border-box; }
  html, body {
    width: 1178px;
    height: 1200px;
    overflow: hidden;
    background: var(--backdrop);
    font-family: "Montserrat", Arial, sans-serif;
  }
  .sign {
    position: absolute;
    left: 118px;
    width: 950px;
    height: 478px;
    overflow: hidden;
  }
  .sign--wide { top: 95px; }
  .sign--stacked { top: 614px; }
  .sign__backdrop {
    position: absolute;
    inset: 0;
    width: 100%;
    height: 100%;
  }
  .row {
    position: absolute;
    left: 0;
    right: 0;
    display: flex;
    align-items: center;
    justify-content: center;
  }
  .brand-name {
    color: var(--white);
    font-weight: 800;
    font-size: 66px;
    letter-spacing: 1px;
    gap: 14px;
  }
  .brand-name__dot {
    width: 26px;
    height: 26px;
    border-radius: 50%;
    background: var(--brand-yellow);
  }
  .offer {
    color: var(--white);
    font-weight: 800;
    letter-spacing: 1px;
    white-space: nowrap;
    line-height: 1;
  }
  .offer__sep {
    display: inline-block;
    border-radius: 50%;
    background: var(--brand-yellow);
    vertical-align: middle;
  }
  .sign--wide .offer { font-size: 70px; gap: 22px; }
  .sign--wide .offer__sep { width: 30px; height: 30px; }
  .sign--stacked .offer { font-size: 58px; gap: 20px; }
  .sign--stacked .offer__sep { width: 24px; height: 24px; }

  .partners { justify-content: space-between; }
  .partner {
    display: flex;
    align-items: center;
    gap: 10px;
    font-weight: 800;
    font-size: 30px;
    white-space: nowrap;
  }
  .partner--meadow { color: var(--brand-blue); }
  .partner--vale { color: var(--ink); }
  .partner__mark {
    width: 22px;
    height: 22px;
    flex: none;
  }
  .partner--meadow .partner__mark { background: var(--brand-yellow); border-radius: 50%; }
  .partner--vale .partner__mark { background: #c0392b; }
  .website {
    font-weight: 700;
    font-size: 34px;
    letter-spacing: 0.5px;
  }
  .website--blue { color: var(--brand-blue); }
  .website--white { color: var(--white); font-weight: 600; }
</style>
</head>
<body>

<section class="sign sign--wide">
  <svg class="sign__backdrop" viewBox="0 0 950 478" preserveAspectRatio="none" aria-hidden="true">
    <rect width="950" height="478" fill="var(--brand-blue)"/>
    <path d="M0 363 Q475 279 950 363 L950 478 L0 478 Z" fill="var(--brand-yellow)"/>
    <path d="M0 375 Q475 291 950 375 L950 478 L0 478 Z" fill="var(--white)"/>
  </svg>

  <div class="row brand-name" style="top:100px;height:80px;">
    <span>Fernowell</span><span class="brand-name__dot"></span>
  </div>

  <div class="row offer" style="top:213px;height:80px;">
    <span>Sales</span><span class="offer__sep"></span><span>Service</span><span class="offer__sep"></span><span>Parts</span>
  </div>

  <div class="row partners" style="top:384px;height:56px;padding:0 54px;">
    <div class="partner partner--meadow"><span class="partner__mark"></span><span>Brook Meadow</span></div>
    <div class="website website--blue">www.fernowell.ie</div>
    <div class="partner partner--vale"><span>Vale</span><span class="partner__mark"></span></div>
  </div>
</section>

<section class="sign sign--stacked">
  <svg class="sign__backdrop" viewBox="0 0 950 478" preserveAspectRatio="none" aria-hidden="true">
    <rect width="950" height="478" fill="var(--brand-blue)"/>
    <path d="M0 231 Q475 313 950 231 L950 431 Q475 351 0 431 Z" fill="var(--brand-yellow)"/>
    <path d="M0 243 Q475 325 950 243 L950 419 Q475 339 0 419 Z" fill="var(--white)"/>
  </svg>

  <div class="row brand-name" style="top:80px;height:76px;font-size:58px;">
    <span>Fernowell</span><span class="brand-name__dot"></span>
  </div>

  <div class="row offer" style="top:172px;height:72px;">
    <span>Sales</span><span class="offer__sep"></span><span>Service</span><span class="offer__sep"></span><span>Parts</span>
  </div>

  <div class="row" style="top:312px;height:60px;gap:150px;">
    <div class="partner partner--meadow" style="font-size:34px;"><span class="partner__mark"></span><span>Brook Meadow</span></div>
    <div class="partner partner--vale" style="font-size:34px;"><span>Vale</span><span class="partner__mark"></span></div>
  </div>

  <div class="row website website--white" style="top:414px;height:48px;">www.fernowell.ie</div>
</section>

</body>
</html>
```